Simple 4 page brochure design - Duplex printable pdf document - A3 format

We are language training company based in France and need :

* Duplex printable pdf document on standard office printer (not professional printer). Once printed, document should fold in two and form a brochure.
* Format : A3 + optional A4 version (European settings)
* Attached zip file contains all elements necessary to complete the work:
- power point specification (written in English and French)
- preliminary design considered as non-satisfactory
- word document with copy / paste content in French and preferred layout
- logos
* Document should be on white background, free of clutter and business like.
* No illustration work necessary, but simple elements of design need to be included to project quality and professionnalism
* We also need an illustration / pictogram for point 4 ('Livret d'apprentissage' which is a learning booklet, to be found in Folder 'Copy Paste Documents' 'Layout and Copy Past' in Word

We need to receive elements within the next 36 to 48 hours to be able to decide on winning design and place order beginning of next week (Monday April 28).

Thank you to all who will take the time to respond.

Reason: Deadline extended to include the whole week-end as no decision will be taken before the beginning of next week.

```html
<!DOCTYPE html>
<html lang="fr">
<head>
<meta charset="utf-8">
<title>Lingua Pont Services – Formations et Services Linguistiques</title>
<link href="https://fonts.googleapis.com/css2?family=Cinzel:wght@400;700&family=Dancing+Script:wght@400;600&family=Great+Vibes&family=Open+Sans:ital,wght@0,400;0,700;1,400&display=swap" rel="stylesheet">
<style>
  :root{
    --green:#8dbf3a;
    --green-dark:#1f9a3f;
    --text:#1d1d1b;
    --white:#ffffff;
    --line:#45a845;
  }
  *{margin:0;padding:0;box-sizing:border-box}
  html,body{width:1200px;height:849px;overflow:hidden;background:var(--white)}
  body{position:relative;font-family:"Open Sans",sans-serif;color:var(--text)}

  .side-band{position:absolute;left:0;top:0;width:44px;height:849px;background:var(--green)}
  .side-band__url{position:absolute;left:22px;top:455px;transform:translate(-50%,-50%) rotate(-90deg);
    white-space:nowrap;color:var(--white);font-weight:700;font-size:21px;letter-spacing:2px;font-family:"Open Sans",sans-serif}

  .panel-title{position:absolute;text-align:center;font-family:"Cinzel",serif;color:var(--green-dark);font-weight:400;line-height:1.25}
  .panel-title .big{font-size:27px}
  .panel-title .small{font-size:21px}
  .title-left{left:120px;width:400px;top:62px}
  .title-right{left:800px;width:330px;top:62px}

  .intro{position:absolute;left:52px;top:150px;width:522px;font-size:10.6px;line-height:1.6}
  .intro p{margin-bottom:4px}
  .intro .lead{font-style:italic;margin-top:8px}

  .pillar{position:absolute;left:52px;width:522px;font-size:10.6px;line-height:1.6}
  .pillar h3{display:flex;align-items:center;gap:10px;font-size:13.5px;font-weight:700;color:var(--green-dark);margin:0 0 6px 20px}
  .pillar h3::after{content:"";flex:1;border-top:2px solid var(--green-dark)}
  .p1{top:305px}.p2{top:397px}.p3{top:493px}.p4{top:572px}

  .partner-box{position:absolute;left:58px;top:668px;width:514px;height:135px;border:2px solid var(--green-dark)}
  .partner-box__brand{position:absolute;left:10px;top:40px;display:flex;align-items:center;gap:6px;
    font-family:"Open Sans",sans-serif;font-weight:700;font-size:20px;color:#1b3f8c}
  .partner-box__brand .dot{width:14px;height:14px;border-radius:50%;background:#5aa7d8}
  .partner-box__text{position:absolute;left:146px;top:20px;width:352px;font-style:italic;font-size:11.4px;line-height:2.2}

  .chain{position:absolute;left:708px;top:98px;height:562px;border-left:2px dotted #2d6a2d}

  .brand-circle{position:absolute;left:645px;top:35px;width:126px;height:126px;border-radius:50%;background:var(--green);
    display:flex;align-items:center;justify-content:center;color:var(--white);font-family:"Open Sans",sans-serif;font-weight:700;font-size:40px;letter-spacing:1px}

  .step{position:absolute;left:708px;width:492px;border-top:3px solid var(--line);border-bottom:3px solid var(--line)}
  .step__circle{position:absolute;left:-63px;top:50%;transform:translateY(-50%);width:126px;height:126px;border-radius:50%;
    background:var(--green);color:var(--white);display:flex;align-items:center;justify-content:center;text-align:center;
    font-family:"Dancing Script",cursive;font-size:17px;line-height:1.3}
  .step__text{position:absolute;left:71px;top:50%;transform:translateY(-50%);width:240px;font-size:11px;line-height:1.6;letter-spacing:.3px}
  .step__partner{position:absolute;left:320px;top:50%;transform:translateY(-50%);width:150px;text-align:center;
    font-family:"Open Sans",sans-serif;font-weight:700;font-size:21px}
  .s1{top:182px;height:108px}.s2{top:335px;height:99px}.s3{top:474px;height:99px}.s4{top:617px;height:101px}
  .partner-a{color:#1d1d1b}.partner-b{color:#2f8fb7}.partner-c{color:#e07b1f}
  .booklet-icon{position:absolute;left:1050px;top:630px;width:66px;height:70px;background:var(--green-dark);opacity:.85}

  .tagline{position:absolute;left:700px;top:765px;width:480px;text-align:center;font-family:"Great Vibes",cursive;
    font-size:40px;color:var(--green-dark)}
</style>
</head>
<body>
  <aside class="side-band"><span class="side-band__url">www.linguapont.fr</span></aside>

  <h1 class="panel-title title-left"><span class="big">Formations</span><br><span class="small">et Services Linguistiques</span></h1>

  <section class="intro">
    <p>Lingua Pont Services (LPS) est une école de langues fondée en 1988, aujourd'hui installée à La Défense, et qui intervient principalement auprès de grands comptes.</p>
    <p>LPS préconise et déploie des dispositifs de formation reposant sur le principe de la mise en situation professionnelle, le seul à même d'augmenter réellement et durablement la capacité des collaborateurs de l'entreprise à pratiquer leur métier dans une langue étrangère (anglais, langue européenne ou langue rare).</p>
    <p class="lead">La démarche de LPS est orientée résultats (opérationnalité et progression des apprenants) et repose sur les piliers suivants :</p>
  </section>

  <section class="pillar p1">
    <h3>L'excellence pédagogique</h3>
    <p>La méthodologie de LPS, une des premières à s'appuyer sur des référentiels de compétences professionnels, a été validée dans la durée par les plus grandes entreprises (Veranor, Nucleis, Banque Terroir, Aerolys, Belcourt, Petramar, Audexa, ...).</p>
  </section>
  <section class="pillar p2">
    <h3>Un corps enseignant expérimenté</h3>
    <p>Nos professeurs, dont certains sont habilités à former des formateurs, disposent d'un double diplôme, universitaire et d'enseignement des langues, souvent complété par un parcours individuel en entreprise.</p>
  </section>
  <section class="pillar p3">
    <h3>Des réponses personnalisées</h3>
    <p>Notre équipe pédagogique dédiée puise dans l'expérience collective de LPS, pédagogique et sectorielle, pour développer des contenus originaux et assurer leur pertinence dans la durée.</p>
  </section>
  <section class="pillar p4">
    <h3>L'intégration des nouvelles technologies</h3>
    <p>LPS s'appuie sur plusieurs outils du marché en fonction des contextes, et développe sur plate-forme propre des parcours en Blended Learning aux contenus personnalisés, parfaitement reliés aux enseignements dispensés dans les modalités traditionnelles.</p>
  </section>

  <div class="partner-box">
    <div class="partner-box__brand"><span class="dot"></span>ParlaNet</div>
    <p class="partner-box__text">LPS est un membre et actionnaire historique de ParlaNet : le 1er réseau qui réunit les meilleurs centres indépendants de formation linguistique en France (26 centres couvrant tout le territoire), avec membres associés dans plusieurs pays européens.</p>
  </div>

  <div class="chain"></div>
  <div class="brand-circle">LPS</div>

  <h2 class="panel-title title-right"><span class="big">Les outils</span><br><span class="small">de déploiement</span></h2>

  <section class="step s1">
    <div class="step__circle">Evaluation<br>linguistique</div>
    <p class="step__text">Une évaluation complète (compréhension orale, écrite, production orale, écrite) reliée aux niveaux du Cadre Européen Commun de Référence.</p>
    <div class="step__partner partner-a">EVALIS</div>
  </section>
  <section class="step s2">
    <div class="step__circle">Determination<br>des besoins</div>
    <p class="step__text">Un recueil automatisé des besoins suivi d'un diagnostic individuel, du positionnement dans le parcours adéquat, de la mise en groupe et accès au modèle économique en temps direct.</p>
    <div class="step__partner partner-b">Besoina</div>
  </section>
  <section class="step s3">
    <div class="step__circle">E-learning</div>
    <p class="step__text">E-learning conçu spécifiquement pour la Banque Terroir, avec des supports diversifiés et des activités motivantes reliées aux objectifs d'apprentissage.</p>
    <div class="step__partner partner-c">Learnova</div>
  </section>
  <section class="step s4">
    <div class="step__circle">Livret<br>d'apprentissage</div>
    <p class="step__text">Un support individuel fourni en début de parcours pour créer le lien entre les différentes modalités.</p>
  </section>
  <div class="booklet-icon" role="img" aria-label="Pictogramme d'un livret d'apprentissage avec crayon"></div>

  <p class="tagline">Votre partenaire linguistique</p>
</body>
</html>
```